Restumping company needs business cards

We need a business card that reflects all the information in the attached file.

Back side to just have the logo (see attached image as an example)

All information to be on the front side

Front side must contain;
Logo
Dale Morrow (Director)
Ph: 1800 472 915
Mob: 0412 687 143
Email: dale@keystonebase.com.au
website: keystonebase.com.au
Call us for a free quote today

Must also contain the words RESTUMPING - SUB FLOOR REPAIRS - RELEVELING

we would like colour scheme to be as per the attached file but open to new suggestions.

Requirements
Must have
• Certified Site Constructor logo
• Crafted Trades Guild Logo
• small snapgrid & pagebook symbol

```html
<!DOCTYPE html>
<html lang="en">
<head>
<meta charset="utf-8">
<title>Keystone Base – Business Cards</title>
<link href="https://fonts.googleapis.com/css2?family=Open+Sans:wght@400;600;700&display=swap" rel="stylesheet">
<style>
  :root{
    --backdrop:#2b2d31;
    --ink:#0c0c0e;
    --paper:#ffffff;
    --violet:#3b3584;
    --steel:#8c8c90;
    --steel-light:#b9b9bd;
    --rule:#5a5a60;
  }
  *{box-sizing:border-box;margin:0;padding:0}
  html,body{width:1200px;height:900px;overflow:hidden;background:var(--backdrop);font-family:"Open Sans",Arial,sans-serif}
  .sheet{position:relative;width:1200px;height:900px}
  .card{position:absolute;left:280px;width:640px;height:390px;border-radius:26px;overflow:hidden}
  .card--front{top:35px;background:var(--paper)}
  .card--back{top:475px;background:var(--ink)}

  /* front */
  .front-top{position:absolute;left:0;top:0;width:100%;height:178px}
  .brand{position:absolute;display:flex;align-items:center;gap:10px}
  .brand__mark{width:22px;height:22px;background:var(--violet)}
  .brand__name{font-weight:700;color:var(--violet);letter-spacing:1px;white-space:nowrap}
  .front-top .brand{left:300px;top:72px}
  .front-top .brand__name{font-size:30px}
  .badge{position:absolute;background:var(--steel-light)}
  .badge--round{left:200px;top:58px;width:38px;height:38px;border-radius:50%}
  .badge--wide{left:196px;top:110px;width:62px;height:22px;border-radius:4px}
  .badge--square{left:318px;top:122px;width:26px;height:26px;border-radius:3px;background:#e3a11c}
  .socials{position:absolute;left:360px;top:126px;display:flex;gap:14px;font-size:11px;color:var(--violet);font-weight:600}
  .socials span{display:flex;align-items:center;gap:5px}
  .socials i{display:block;width:10px;height:10px;border-radius:50%;background:var(--violet)}

  .front-band{position:absolute;left:0;top:178px;width:100%;height:152px;background:var(--ink)}
  .person{position:absolute;left:60px;top:34px;text-align:right;width:250px}
  .person__name{font-size:28px;font-weight:600;color:var(--steel);letter-spacing:1px;text-transform:uppercase}
  .person__role{font-size:15px;color:var(--violet);letter-spacing:1px;margin-top:6px;text-transform:uppercase}
  .divider{position:absolute;left:336px;top:18px;width:1px;height:116px;background:var(--rule)}
  .contacts{position:absolute;left:356px;top:20px;list-style:none}
  .contacts li{display:flex;align-items:center;gap:10px;font-size:15px;color:var(--steel);height:28px}
  .contacts svg{width:14px;height:14px;fill:var(--violet)}

  .front-foot{position:absolute;left:0;top:330px;width:100%;height:60px;background:var(--violet);border-top:2px solid var(--steel-light)}
  .front-foot p{position:absolute;left:60px;top:16px;font-size:17px;color:var(--steel-light)}

  /* back */
  .card--back .brand{left:50%;top:130px;transform:translateX(-50%)}
  .card--back .brand__name{font-size:44px}
  .card--back .brand__mark{width:30px;height:30px}
  .back-rule{position:absolute;left:200px;top:200px;width:240px;height:1px;background:var(--steel)}
  .services{position:absolute;left:0;top:240px;width:100%;text-align:center;font-size:17px;font-weight:600;color:var(--steel);letter-spacing:1.5px}
</style>
</head>
<body>
<main class="sheet">

  <section class="card card--front">
    <div class="front-top">
      <div class="badge badge--round" aria-label="Certified Site Constructor badge"></div>
      <div class="badge badge--wide" aria-label="Trade association member badge"></div>
      <div class="brand">
        <span class="brand__mark"></span>
        <span class="brand__name">KEYSTONE BASE</span>
      </div>
      <div class="badge badge--square" aria-label="Crafted Trades Guild badge"></div>
      <div class="socials">
        <span><i></i>snapgrid</span>
        <span><i></i>pagebook</span>
      </div>
    </div>

    <div class="front-band">
      <div class="person">
        <p class="person__name">Dale Morrow</p>
        <p class="person__role">Director</p>
      </div>
      <div class="divider"></div>
      <ul class="contacts">
        <li><svg viewBox="0 0 24 24"><path d="M6.6 10.8a15 15 0 0 0 6.6 6.6l2.2-2.2a1 1 0 0 1 1-.25 11.4 11.4 0 0 0 3.6.6 1 1 0 0 1 1 1V20a1 1 0 0 1-1 1A17 17 0 0 1 3 4a1 1 0 0 1 1-1h3.5a1 1 0 0 1 1 1c0 1.25.2 2.45.6 3.6a1 1 0 0 1-.25 1z"/></svg>1800 472 915</li>
        <li><svg viewBox="0 0 24 24"><path d="M7 2h10a2 2 0 0 1 2 2v16a2 2 0 0 1-2 2H7a2 2 0 0 1-2-2V4a2 2 0 0 1 2-2zm0 3v13h10V5zm5 14.2a1 1 0 1 0 0 .01z"/></svg>0412 687 143</li>
        <li><svg viewBox="0 0 24 24"><path d="M3 5h18v14H3zm2 2v.5l7 4.5 7-4.5V7zm0 2.9V17h14V9.9l-7 4.5z"/></svg>dale@keystonebase.com.au</li>
        <li><svg viewBox="0 0 24 24"><path d="M12 2a10 10 0 1 0 0 20 10 10 0 0 0 0-20zm6.9 9h-3a15 15 0 0 0-1.3-5.6A8 8 0 0 1 18.9 11zM12 4.1c.9 1.2 1.8 3.6 1.9 6.9h-3.8c.1-3.3 1-5.7 1.9-6.9zM9.4 5.4A15 15 0 0 0 8.1 11h-3a8 8 0 0 1 4.3-5.6zM5.1 13h3a15 15 0 0 0 1.3 5.6A8 8 0 0 1 5.1 13zm6.9 6.9c-.9-1.2-1.8-3.6-1.9-6.9h3.8c-.1 3.3-1 5.7-1.9 6.9zm2.6-1.3a15 15 0 0 0 1.3-5.6h3a8 8 0 0 1-4.3 5.6z"/></svg>keystonebase.com.au</li>
      </ul>
    </div>

    <div class="front-foot">
      <p>Call us for a free quote today</p>
    </div>
  </section>

  <section class="card card--back">
    <div class="brand">
      <span class="brand__mark"></span>
      <span class="brand__name">KEYSTONE BASE</span>
    </div>
    <div class="back-rule"></div>
    <p class="services">RESTUMPING &nbsp;|&nbsp; SUB FLOOR REPAIRS &nbsp;|&nbsp; RELEVELING</p>
  </section>

</main>
</body>
</html>
```